The Academy for Stewardship in Civic Builds' 2024 Lift Her Up Summit: Spark Venture needs a full page flyer that can be converted to a website header.

Date: February, 16, 2024
Location: Harborline Lodge Meeting Hall, San Marcos, TX

ABOUT THE FORUM

Dedicated to celebrating the entrepreneurial spirit and unwavering determination of women, the Lift Her Up Summit proudly presents, “Spark Venture.” Here, we believe in the power of dreams, the strength of innovation, and the impact of women-led endeavors.

Join us at this dynamic Forum as we explore the world of Passion Projects – those inspiring ventures, including YOURSELF, fueled by creativity, ambition, and a deep-seated love for what we do. Whether you're an seasoned expert, a budding visionary, or simply an enthusiast eager to learn and grow, this Forum is your hub for all things related to the fusion of passion and business.

WHAT TO EXPECT

Inspiring Stories: Immerse yourself in a collection of captivating success stories and personal journeys that highlight the incredible feats achieved through passion-driven initiatives. Learn from remarkable women who turned their dreams into reality and gain insights into their strategies, challenges, and triumphs.

Expert Insights: Discover the art of transforming a passion into a sustainable business model. Our forum gathers experts and thought leaders across the AEC community (and more) to share invaluable advice, practical tips, and proven strategies, guiding you along the exciting journey of pursuing your passion.

Networking Opportunities: Connect with like-minded individuals who share your passion for making a difference. Engage in lively discussions, exchange ideas, and build meaningful relationships with fellow forum participants, potential collaborators, and mentors who can help elevate your Spark Venture.

Interactive Workshops: Participate in hands-on workshops designed to enhance your skills, from refining your business plan to mastering effective marketing techniques. These immersive sessions are tailored to address the unique challenges faced by women in the design and construction industry and will empower you to overcome obstacles with confidence.

Passion Showcase: Elevate your project's visibility by showcasing your Spark Venture to the Forum. Receive feedback, support, and perhaps even connect with individuals who are excited to collaborate and join you on your journey.

Empowerment and Support: Embrace a supportive community that believes in your potential and is committed to fostering an inclusive environment. Share your highs and lows, seek advice, and find encouragement to keep pursuing your passion, no matter the hurdles.

Join Us!

Whether you're taking your first steps toward transforming your passion into a business or are seeking to amplify the impact of your existing venture, or just personal improvement, the Lift Her Up Summit: "Spark Venture" is your gateway to inspiration, knowledge, and connection. Let's come together, celebrate the strength of women-led endeavors, and empower one another to turn our passions into legacies that shape the future.

Target Market(s)

Professionals in the design and construction industry.

Industry/Entity Type

Design and Construction

Requirements
Must have
• A-StCB logo
Nice to have
• Title, Date, Location, Graphics that fit the theme of the the Forum: Spark Venture, and the mission of the organization.
Should not have
• Full description of event should be in the graphic.

```html
<!DOCTYPE html>
<html lang="en">
<head>
<meta charset="utf-8">
<title>Lift Her Up Summit: Spark Venture</title>
<link rel="stylesheet" href="https://fonts.googleapis.com/css2?family=Josefin+Sans:wght@600;700&family=Ubuntu:wght@400;500;700&display=swap">
<style>
:root{
  --blue:#37509b;
  --green:#8db33f;
  --ink:#1f1f1f;
  --grey:#4a4a4a;
  --white:#ffffff;
}
*{margin:0;padding:0;box-sizing:border-box}
html,body{width:927px;height:1200px;overflow:hidden;background:var(--white)}
.flyer{position:relative;width:927px;height:1200px;overflow:hidden;font-family:"Ubuntu",sans-serif;color:var(--ink)}
.hero-photo{position:absolute;left:0;top:0;width:927px;height:500px;
  background:linear-gradient(90deg,#f2f3f5 0%,#e4e7ec 45%,#c9ced6 70%,#d9a17e 78%,#cfd4dc 88%,#e6e9ee 100%)}
.pattern-bg{position:absolute;left:0;top:491px;width:927px;height:709px;
  background:linear-gradient(115deg,#ffffff 0%,#ffffff 45%,#e3efc2 62%,#a9d68c 78%,#5cc6a5 90%,#6bc9e6 100%)}
.pattern-bg.low{top:1043px;left:0;width:360px;height:157px;
  background:linear-gradient(200deg,#f3f8e4 0%,#c7e39a 45%,#63c39a 85%,#3fbcb0 100%)}
.shapes{position:absolute;left:0;top:0}
.brand{position:absolute;left:43px;top:100px;display:flex;align-items:center;gap:14px}
.brand-mark{width:34px;height:34px;background:var(--blue)}
.brand-name{font-family:"Ubuntu",sans-serif;font-weight:500;font-size:40px;color:var(--grey);line-height:1}
.edition{position:absolute;left:43px;top:223px;width:473px;height:53px;background:var(--green);color:var(--white);
  font-family:"Josefin Sans",sans-serif;font-weight:600;font-size:14.5px;display:flex;align-items:center;justify-content:center;padding-top:3px;white-space:nowrap}
.title{position:absolute;left:43px;top:302px;font-family:"Josefin Sans",sans-serif;font-weight:700;font-size:40px;line-height:48px;color:var(--white)}
.when-where{position:absolute;right:46px;top:386px;text-align:right;font-family:"Josefin Sans",sans-serif;font-weight:700;color:var(--blue)}
.date{font-size:28px;line-height:30px}
.venue{font-size:18px;line-height:24px;margin-top:2px}
.h2{position:absolute;left:45px;font-family:"Josefin Sans",sans-serif;font-weight:700;font-size:26px;color:var(--green)}
.about-h{top:516px}
.about{position:absolute;left:45px;top:550px;width:840px;font-size:15.3px;line-height:22px;text-align:justify}
.about p+p{margin-top:22px}
.expect-h{top:759px}
.circle{position:absolute;top:797px;width:126px;height:126px;border-radius:50%;display:flex;align-items:center;justify-content:center;text-align:center;
  color:var(--white);font-weight:500;font-size:15.5px;line-height:22px}
.circle::before{content:"";position:absolute;inset:8px;border:1.5px solid var(--white);border-radius:50%}
.circle.blue{background:var(--blue)}
.circle.green{background:var(--green)}
.circle.small{font-size:13px;line-height:19px}
.join{position:absolute;left:40px;top:952px;font-family:"Josefin Sans",sans-serif;font-weight:700;font-size:68px;color:var(--white);letter-spacing:-1px}
.closing{position:absolute;left:353px;top:1027px;width:518px;color:var(--white);font-size:19px;line-height:25.5px;text-align:justify}
.closing strong{font-weight:700}
</style>
</head>
<body>
<div class="flyer">
  <div class="hero-photo" role="img" aria-label="Photo of a businesswoman in a blazer with a city skyline and colleagues in the background"></div>
  <div class="pattern-bg" role="img" aria-label="Soft green and teal triangle pattern"></div>
  <div class="pattern-bg low" role="img" aria-label="Soft green and teal triangle pattern"></div>

  <svg class="shapes" width="927" height="1200" viewBox="0 0 927 1200" aria-hidden="true">
    <polygon points="0,250 609,250 467,449 0,449" fill="var(--blue)"/>
    <polygon points="535,366 927,366 927,491 451,491" fill="var(--green)"/>
    <polygon points="0,944 374,944 303,1043 0,1043" fill="var(--green)"/>
    <polygon points="349,1006 927,1006 927,1200 209,1200" fill="var(--blue)"/>
  </svg>

  <div class="brand">
    <div class="brand-mark"></div>
    <div class="brand-name">A-StCB</div>
  </div>

  <div class="edition">THE ACADEMY FOR STEWARDSHIP IN CIVIC BUILDS’ 2024</div>
  <h1 class="title">LIFT HER UP SUMMIT<br>"SPARK VENTURE"</h1>

  <div class="when-where">
    <div class="date">FEBRUARY, 16, 2024</div>
    <div class="venue">HARBORLINE LODGE MEETING HALL<br>SAN MARCOS, TX</div>
  </div>

  <h2 class="h2 about-h">ABOUT THE FORUM</h2>
  <div class="about">
    <p>Dedicated to celebrating the entrepreneurial spirit and unwavering determination of women, the Lift Her Up Summit proudly presents, “Spark Venture.” Here, we believe in the power of dreams, the strength of innovation, and the impact of women-led endeavors.</p>
    <p>Join us at this dynamic Forum as we explore the world of Passion Projects – those inspiring ventures, including YOURSELF, fueled by creativity, ambition, and a deep-seated love for what we do. Whether you're an seasoned expert, a budding visionary, or simply an enthusiast eager to learn and grow, this Forum is your hub for all things related to the fusion of passion and business.</p>
  </div>

  <h2 class="h2 expect-h">WHAT TO EXPECT</h2>
  <div class="circle blue" style="left:59px">Inspiring<br>Stories</div>
  <div class="circle green" style="left:196px">Expert<br>Insights</div>
  <div class="circle blue small" style="left:333px;font-size:14px">Networking<br>Opportunities</div>
  <div class="circle green" style="left:468px">Interactive<br>Workshops</div>
  <div class="circle blue" style="left:602px">Passion<br>Showcase</div>
  <div class="circle green small" style="left:737px">Empowerment<br>and Support</div>

  <div class="join">JOIN US!</div>
  <p class="closing">Whether you're taking your first steps toward transforming your passion into a business or are seeking to amplify the impact of your existing venture, or just personal improvement, the Lift Her Up <strong>Summit: "Spark Venture"</strong> is your gateway to inspiration, knowledge, and connection.</p>
</div>
</body>
</html>
```